Design a "healthy, happy dog and cat" cheque/check background

I am looking for a few design concepts featuring a happy healthy dog and cat, that will be used as the background of a paper cheque/check.

This will require Photoshop and stock photos.

Here is the design brief: https://files.brivontel.net/sheet/48kQmZ2xTrWvLpN7aHcYeJ5uBdFsKo9GiRtXnVw3Lz/view?share=on

Colors

Designer to choose colors to be used in the design.

Requirements
Must have
• A happy dog and cat the main focus within the "empty" central part of the cheque/check, and a complementary background for the rest of the cheque, following the design guidelines in the attached google doc.

```html
<!DOCTYPE html>
<html lang="en">
<head>
<meta charset="utf-8">
<title>Personal Cheque – Dog and Cat Background</title>
<link href="https://fonts.googleapis.com/css2?family=Roboto:wght@400;700;900&family=Montserrat:wght@500;600&family=Share+Tech+Mono&display=swap" rel="stylesheet">
<style>
  :root {
    --backdrop: #82939a;
    --paper: #ffffff;
    --ink: #1a1a1a;
    --ink-soft: #3b3b3b;
    --rule: #2a2a2a;
    --photo-warm: #f7ecd6;
    --photo-peach: #f3dcc8;
    --photo-blue: #dfe6ef;
  }
  * { margin: 0; padding: 0; box-sizing: border-box; }
  html, body {
    width: 1200px; height: 1200px; overflow: hidden;
    background: var(--backdrop);
  }
  .canvas { position: relative; width: 1200px; height: 1200px; }
  .cheque {
    position: absolute; left: 2px; top: 329px;
    width: 1198px; height: 543px;
    background: var(--paper);
    font-family: "Roboto", Arial, sans-serif;
    color: var(--ink);
  }
  .pet-photo {
    position: absolute; left: 374px; top: 47px;
    width: 642px; height: 358px;
    background:
      radial-gradient(ellipse at 48% 30%, var(--photo-peach) 0%, transparent 45%),
      radial-gradient(ellipse at 80% 55%, var(--photo-blue) 0%, transparent 45%),
      linear-gradient(180deg, #fdf8ef 0%, var(--photo-warm) 100%);
    opacity: .85;
    border-radius: 40px 40px 0 0;
  }
  .abs { position: absolute; white-space: nowrap; }
  .cheque-number { left: 1023px; top: 42px; font-size: 28px; font-weight: 700; }
  .account-holder { left: 57px; top: 59px; line-height: 1.1; color: var(--ink-soft); }
  .account-holder .name { font-size: 23px; font-weight: 900; letter-spacing: .3px; }
  .account-holder .line { font-size: 20px; }
  .date-label { left: 783px; top: 110px; font-size: 21px; }
  .date-format { left: 866px; top: 130px; font-size: 15px; letter-spacing: 0; word-spacing: 0; }
  .date-format span { display: inline-block; width: 37.6px; }
  .payee-label { left: 56px; top: 189px; font-size: 15px; line-height: 14px; }
  .dollar-sign { left: 946px; top: 184px; font-size: 28px; }
  .amount-words { left: 918px; top: 250px; font-size: 16px; }
  .institution { left: 152px; top: 298px; font-family: "Montserrat", Arial, sans-serif; line-height: 19px; }
  .institution .name { font-size: 19px; font-weight: 600; }
  .institution .line { font-size: 18px; font-weight: 500; letter-spacing: 1px; }
  .institution-mark {
    position: absolute; left: 62px; top: 290px;
    width: 78px; height: 78px; border-radius: 50%; background: var(--ink);
  }
  .company-name { left: 809px; top: 340px; font-size: 16px; }
  .memo-label { left: 61px; top: 382px; font-size: 13px; }
  .micr {
    left: 55px; top: 445px; font-family: "Share Tech Mono", monospace;
    font-size: 30px; letter-spacing: 5px; color: #111;
  }
  .rules { position: absolute; left: 0; top: 0; }
  .security-badge {
    position: absolute; left: 1160px; top: 272px; width: 32px; height: 134px;
    border: 1.5px dashed var(--ink);
  }
  .security-badge .caption {
    position: absolute; left: 2px; top: 70px; transform: rotate(-90deg); transform-origin: left top;
    font-size: 7px; line-height: 8px; white-space: nowrap;
  }
  .security-badge .code { position: absolute; left: 4px; top: 105px; font-size: 7px; }
  .security-badge .mark { position: absolute; left: 8px; top: 116px; width: 14px; height: 12px; background: var(--ink); }
</style>
</head>
<body>
<div class="canvas">
  <section class="cheque">
    <div class="pet-photo" role="img" aria-label="Faded photograph of a smiling child hugging a happy dog and a Siamese cat"></div>

    <div class="abs cheque-number">101</div>

    <div class="abs account-holder">
      <div class="name">Northgate Cheque Co. Personal Cheque</div>
      <div class="line">15 Residential Street</div>
      <div class="line">Toronto, Ontario M1M 1M1</div>
    </div>

    <div class="abs date-label">DATE</div>
    <div class="abs date-format"><span>D</span><span>D</span><span>M</span><span>M</span><span>Y</span><span>Y</span><span>Y</span><span>Y</span></div>

    <div class="abs payee-label">PAY TO THE<br>ORDER OF</div>
    <div class="abs dollar-sign">$</div>
    <div class="abs amount-words">100 DOLLARS</div>

    <div class="institution-mark"></div>
    <div class="abs institution">
      <div class="name">Your Financial Institution</div>
      <div class="line">200 Finance Avenue</div>
      <div class="line">Your City, Your Province A1B 2CS</div>
    </div>

    <div class="abs company-name">Optional Company Name</div>
    <div class="abs memo-label">MEMO</div>

    <svg class="rules" width="1198" height="543" viewBox="0 0 1198 543">
      <g stroke="var(--rule)" stroke-width="1.3" fill="none">
        <line x1="56" y1="222" x2="922" y2="222"/>
        <line x1="922" y1="191" x2="922" y2="222"/>
        <line x1="58" y1="275" x2="905" y2="275"/>
        <line x1="905" y1="275" x2="911" y2="240"/>
        <line x1="60" y1="397" x2="586" y2="397"/>
        <line x1="686" y1="397" x2="1098" y2="397"/>
      </g>
    </svg>

    <div class="security-badge">
      <div class="caption">Details on Back<br>Détails au Verso</div>
      <div class="code">0803</div>
      <div class="mark"></div>
    </div>

    <div class="abs micr">⑈101⑈ ⑆12345⑉678⑆ 12345⑉6789⑈</div>
  </section>
</div>
</body>
</html>
```